Bus. Card/Envelope/Letterhead Design Request with my Logo

I have a logo created. I need to create a business card design, letterhead design and envelope design with the new logo.
Updates

The logo has now been posted. Thank you.

Target Market(s)

Professional. Legal Field.

Industry/Entity Type

Business

Requirements
Must have
• I like the same font as the logo.

```html
<!DOCTYPE html>
<html lang="en">
<head>
<meta charset="utf-8">
<title>Donnelly Kerrigan LLP – Business Card</title>
<link rel="stylesheet" href="https://fonts.googleapis.com/css2?family=Arimo&family=Cormorant+Garamond:wght@500&family=Lato&family=Open+Sans&display=swap">
<style>
  :root {
    --brand-green: #77dd00;
    --ink: #1d1d1b;
    --ink-soft: #7b7b7b;
    --paper: #ffffff;
    --card-edge: #dcdcdc;
    --frame: #000000;
  }
  * { margin: 0; padding: 0; box-sizing: border-box; }
  html, body { width: 1200px; height: 779px; overflow: hidden; background: var(--paper); }
  .canvas { position: relative; width: 1200px; height: 779px; }

  .board {
    position: absolute; left: 0; top: 0; width: 1200px; height: 713px;
    border: 1px solid var(--frame);
  }

  .card-front {
    position: absolute; left: 47px; top: 82px; width: 649px; height: 404px;
    background: var(--brand-green); border: 1px solid #b9d99a;
    display: flex; align-items: center; justify-content: center; gap: 16px;
  }
  .card-front .mark-dot { width: 34px; height: 34px; border-radius: 50%; background: var(--paper); flex: none; }
  .card-front .firm-name {
    font-family: "Lato", Arial, sans-serif; font-weight: 400;
    font-size: 34px; color: var(--paper);
  }

  .card-back {
    position: absolute; left: 696px; top: 24px; width: 407px; height: 649px;
    background: var(--paper); border: 1px solid var(--card-edge);
  }
  .card-back > * { position: absolute; }
  .firm-lockup {
    left: 0; width: 100%; top: 72px;
    display: flex; align-items: center; justify-content: center; gap: 12px;
  }
  .firm-lockup .mark-dot { width: 22px; height: 22px; border-radius: 50%; background: var(--brand-green); flex: none; }
  .firm-lockup .firm-name {
    font-family: "Lato", Arial, sans-serif; font-weight: 400;
    font-size: 27px; color: var(--ink);
  }

  .person-name {
    left: 0; width: 100%; top: 214px; text-align: center;
    font-family: "Cormorant Garamond", Georgia, serif; font-weight: 500;
    font-size: 38px; color: var(--brand-green); letter-spacing: 1px;
  }
  .person-role {
    left: 0; width: 100%; top: 262px; text-align: center;
    font-family: "Open Sans", Arial, sans-serif; font-size: 23px; color: #000;
  }
  .rule-green { left: 29px; top: 300px; width: 348px; height: 3px; background: var(--brand-green); }

  .contact, .address, .website {
    font-family: "Lato", Arial, sans-serif; font-size: 19px; color: var(--ink-soft); line-height: 1;
  }
  .contact { left: 0; width: 100%; text-align: center; }
  .contact-email { top: 341px; }
  .contact-phone { top: 375px; }
  .address { left: 84px; top: 493px; line-height: 25px; }
  .website { left: 0; width: 100%; top: 623px; text-align: center; }
  .card-back .contact-email { top: 318px; }
  .card-back .contact-phone { top: 352px; }
  .card-back .address { top: 472px; }
  .card-back .website { top: 598px; }

  .label {
    position: absolute; font-family: "Arimo", Arial, sans-serif; font-size: 60px; color: #000; line-height: 1;
  }
  .label-front { left: 154px; top: 628px; }
  .label-back { left: 767px; top: 722px; }
</style>
</head>
<body>
<main class="canvas">
  <div class="board"></div>

  <section class="card-front" aria-label="Front of card">
    <span class="mark-dot"></span>
    <span class="firm-name">Donnelly Kerrigan LLP</span>
  </section>

  <section class="card-back" aria-label="Back of card">
    <div class="firm-lockup">
      <span class="mark-dot"></span>
      <h1 class="firm-name">Donnelly Kerrigan LLP</h1>
    </div>

    <h2 class="person-name">NAME</h2>
    <p class="person-role">DESIGNATION</p>
    <span class="rule-green"></span>

    <p class="contact contact-email">abcdefgh@donnellykerrigan.com</p>
    <p class="contact contact-phone">oxoxoxoxoxoxoxo : Phone</p>

    <p class="address">This the space for address,<br>not the actual content</p>

    <p class="website">www.examplesiteaddress.com</p>
  </section>

  <p class="label label-front">Front card</p>
  <p class="label label-back">Back card</p>
</main>
</body>
</html>
```